We need a new design/function for our reusable Sandwich paper bag

1. We need a designer who can help us create a design and improve the functionality of our paper lunch bag (image attached) and create "a new design for our new sandwich paper bag".

We would like to see designs for people age +18 ( working men, collage). The sandwich paper bag design should have a zipper (colored zipper is available) at the top, the sandwich bag dimension will be 8.5 x7.75x 1.5 in

2. The designer must also design a simple package cover for the sandwich bag

The feature of the material that will be used in manufacturing the sandwich paper bag: It combines the advantages of paper, film, and weaving. It is thinner than paper, but it is tough and tear resistant, texture and touch. Unique, waterproof, anti-fouling and weather-resistant, environmentally friendly and recyclable, has been widely used in textile

Target Market(s)

USA, Canada

Colors

Designer to choose colors to be used in the design.

Requirements
Must have
• Design for the sandwich paper bag
• Package design for the sandwich bag
• The designer must remember that there should be a zipper at the top of the bag
• Kindly find a suitable and small place to put our logo in it, besides the bag
Nice to have
• Try to design something that covers the crumpled paper bag look or appear it in a fashion way
• We appreciate if we can see an improvement in the functionality of the paper sandwich bag, not only the design. We need a new idea on how people will use this bag
Should not have
• Please don't use food images in your design

```html
<!DOCTYPE html>
<html lang="en">
<head>
<meta charset="utf-8">
<title>Sandwich Bag Package Cover</title>
<link rel="stylesheet" href="https://fonts.googleapis.com/css2?family=Open+Sans:wght@400;700;800&display=swap">
<style>
  :root {
    --paper: #c8d2cf;
    --ink: #111111;
    --brand-red: #b31c2e;
    --white: #ffffff;
    --fold: #1a1a1a;
  }
  * { margin: 0; padding: 0; box-sizing: border-box; }
  html, body { width: 1200px; height: 253px; overflow: hidden; background: var(--paper); }
  .cover {
    position: relative;
    width: 1200px;
    height: 253px;
    background: radial-gradient(ellipse at 30% 40%, #d0d9d6 0%, var(--paper) 60%, #c2ccc9 100%);
    font-family: "Open Sans", Arial, sans-serif;
    color: var(--ink);
    overflow: hidden;
  }
  .fold-line {
    position: absolute; left: 600px; top: 0; width: 1px; height: 218px; background: var(--fold);
  }
  .base-band {
    position: absolute; left: 0; top: 218px; width: 1200px; height: 35px; background: var(--brand-red);
  }
  .base-band::after {
    content: ""; position: absolute; left: 600px; top: 0; width: 1px; height: 35px; background: var(--fold);
  }
  .brand-dot {
    position: absolute; left: 280px; top: 21px; width: 36px; height: 36px;
    border-radius: 50%; border: 2px solid var(--ink);
  }
  .brand-name {
    position: absolute; left: 190px; top: 62px; width: 220px;
    text-align: center; font-weight: 800; line-height: 1;
  }
  .brand-name .line-one { display: block; font-size: 42px; letter-spacing: 0.5px; }
  .brand-name .line-two {
    display: flex; align-items: center; justify-content: center; gap: 8px;
    font-size: 42px; margin-top: 3px;
  }
  .brand-name .dash { width: 35px; height: 4px; background: var(--ink); }
  .flourish { position: absolute; background: #2a2a2a; opacity: 0.75; border-radius: 4px; }
  .flourish-brand { left: 241px; top: 146px; width: 118px; height: 9px; }
  .flourish-small { width: 69px; height: 6px; }
  .skyline {
    position: absolute; left: 119px; top: 196px; width: 364px; height: 22px;
    background: linear-gradient(to bottom, #c0303f, var(--brand-red));
  }
  .slogan {
    position: absolute; left: 198px; top: 222px; width: 206px;
    font-size: 16.5px; font-weight: 700; color: var(--white); text-align: center; white-space: nowrap;
  }
  .info { position: absolute; left: 658px; width: 477px; }
  .info h2 { font-size: 10.5px; font-weight: 800; letter-spacing: 0.1px; line-height: 1; }
  .info .flourish-small { position: static; display: block; margin: 6px 0 5px; }
  .info p {
    font-size: 9px; line-height: 14px; text-align: justify; letter-spacing: -0.05px;
  }
  .info-instruction { top: 38px; }
  .info-precaution { top: 123px; }
</style>
</head>
<body>
<main class="cover">
  <section class="front-panel">
    <span class="brand-dot"></span>
    <h1 class="brand-name">
      <span class="line-one">COMPANY</span>
      <span class="line-two"><span class="dash"></span>NAME<span class="dash"></span></span>
    </h1>
    <div class="flourish flourish-brand" role="img" aria-label="Decorative scroll ornament"></div>
    <div class="skyline" role="img" aria-label="Red city skyline silhouette"></div>
  </section>

  <div class="fold-line"></div>
  <div class="base-band"></div>
  <p class="slogan">YOUR SLOGAN GOES HERE</p>

  <section class="back-panel">
    <div class="info info-instruction">
      <h2>INSTRUCTION</h2>
      <div class="flourish flourish-small" role="img" aria-label="Small decorative scroll ornament"></div>
      <p>Lorem Ipsum is simply dummy text of the printing and typesetting industry. Lorem Ipsum has been the industry's standard dummy text ever since the 1500s, when an unknown printer took a galley of type and scrambled it to make a type specimen book.</p>
    </div>
    <div class="info info-precaution">
      <h2>PRECAUTION</h2>
      <div class="flourish flourish-small" role="img" aria-label="Small decorative scroll ornament"></div>
      <p>Lorem Ipsum is simply dummy text of the printing and typesetting industry. Lorem Ipsum has been the industry's standard dummy text ever since the 1500s, when an unknown printer took a galley of type and scrambled it to make a type specimen book.</p>
    </div>
  </section>
</main>
</body>
</html>
```